Zielgruppe
Seminare, Vorträge , Therapien, Beratung, Coaching
WEchseljahre Beratung
Sexualtherapie, Sexualberatung
Mentaltraining
Es soll Frauen gefallen und ermuntern zum Seminar zu kommen, frü Thema Wechseljahre interessieren
Aufgabenstellung
Grösse A5 Hochkant

```html
<!DOCTYPE html>
<html lang="de">
<head>
<meta charset="utf-8">
<title>Wechseljahre Seminar Plakat</title>
<link rel="stylesheet" href="https://fonts.googleapis.com/css2?family=Italiana&family=Open+Sans:wght@400;600&display=swap">
<style>
  :root {
    --ink: #1e1e1e;
    --body: #555555;
    --rose: #d58db0;
    --rose-deep: #cf7fa6;
    --sky: #a9dbe8;
    --turquoise: #4cc8e0;
    --lavender: #a7a9cf;
    --paper: #fdfbfc;
    --blush: #f6e9ef;
    --bg: #ffffff;
  }
  html, body { margin: 0; padding: 0; overflow: hidden; background: var(--bg); }
  .poster {
    position: relative; width: 872px; height: 1200px; overflow: hidden;
    background: var(--paper);
    font-family: "Open Sans", sans-serif; color: var(--body);
  }
  .backdrop { position: absolute; inset: 0; }
  .panel-left {
    position: absolute; left: 29px; top: 0; width: 388px; height: 1200px;
    background: var(--paper);
  }
  .rule { position: absolute; left: 47px; width: 360px; height: 2px; background: var(--rose); }
  .rule::before {
    content: ""; position: absolute; left: -10px; top: -9px; width: 20px; height: 20px;
    border-radius: 50%; background: var(--rose);
  }
  h2 {
    position: absolute; margin: 0; font-family: "Italiana", serif; font-weight: 400;
    color: var(--ink); font-size: 29px; line-height: 30px;
  }
  ul { position: absolute; margin: 0; padding: 0; list-style: none; font-size: 16.5px; line-height: 24px; }
  ul li { position: relative; padding-left: 18px; }
  ul li::before { content: "-"; position: absolute; left: 0; }
  .pink { color: var(--rose-deep); }
  p { position: absolute; margin: 0; font-size: 16.5px; line-height: 24px; }
  .contact { color: var(--ink); font-size: 16.5px; line-height: 24px; }
  .contact strong { font-weight: 600; }
  .name { font-size: 19px; }
  .details {
    position: absolute; left: 597px; width: 270px; text-align: center;
    color: var(--ink); font-size: 16.5px; line-height: 22px; transform: translateX(-135px);
  }
  .portrait {
    position: absolute; left: 660px; top: 470px; width: 212px; height: 570px;
    background: radial-gradient(ellipse at 65% 45%, #e8c2a8 0%, #d9b7a4 30%, #cfd6dc 65%, rgba(240,246,250,0) 100%);
  }
  .badge {
    position: absolute; left: 420px; top: 833px; width: 322px; height: 322px; border-radius: 50%;
    background: #d98fb4; border: 6px solid #ffffff; box-sizing: border-box;
    display: flex; align-items: center; justify-content: center;
  }
  .badge p {
    position: static; width: 250px; text-align: center; color: #ffffff;
    font-size: 16.5px; line-height: 20px; margin-top: -30px;
  }
</style>
</head>
<body>
<div class="poster">
  <svg class="backdrop" width="872" height="1200" viewBox="0 0 872 1200" aria-hidden="true">
    <rect x="0" y="0" width="29" height="1200" fill="#bfe3ee"/>
    <path d="M0 150 Q15 110 29 90 L29 400 Q10 350 0 330 Z" fill="var(--blush)"/>
    <rect x="0" y="1040" width="29" height="14" fill="var(--turquoise)"/>
    <path d="M417 0 H872 V105 Q720 50 560 20 Q480 8 417 30 Z" fill="var(--blush)"/>
    <path d="M560 0 H872 V165 Q800 170 720 120 Q640 60 560 0 Z" fill="var(--sky)"/>
    <path d="M417 1095 Q560 1080 700 1040 Q800 1010 872 975 V1200 H417 Z" fill="var(--turquoise)"/>
    <path d="M417 1110 Q580 1100 720 1060 Q810 1030 872 995 V1200 H417 Z" fill="var(--lavender)"/>
  </svg>

  <div class="panel-left"></div>

  <div class="rule" style="top:36px"></div>
  <h2 style="left:47px; top:52px">Kennen Sie diese Fragen?</h2>
  <ul style="left:47px; top:104px; width:370px">
    <li>Wechseljahre, was heisst das für mich? Was passiert gerade mit mir?</li>
    <li>Was möchte ich vom Leben, welche Träume und Wünsche habe ich?</li>
    <li>Was kann ich für mich in dieser Zeit tun?</li>
    <li>Weshalb stelle ich so vieles in Frage und grübele?</li>
    <li>Weshalb kann ich so schlecht einschlafen oder durchschlafen?</li>
    <li>Soll ich Hormone nehmen, was gibt es sonst noch für Möglichkeiten?</li>
  </ul>

  <h2 style="left:47px; top:398px; width:370px">Ein Neuwerden, ein Loslassen, ein einzigartiges Geschenk und Herausforderung zugleich!</h2>
  <p style="left:47px; top:505px; width:370px">Viele Frauen befinden, dass mit dem Klimakterium eine Last von ihren Schultern fällt. Endlich dürfen sie sich fallen lassen, endlich an sich selbst denken. Für solche Frauen beginnt mit den hormonellen Wallungen eine Phase des Perspektiv­wechsels. Die Zeit des Klimakteriums lädt zu einer inneren Inventur und gegebenenfalls einer Neuorientierung ein.</p>
  <p class="pink" style="left:47px; top:742px; width:372px">Statt von einem Gefühlschaos überwältigt zu werden, empfinden sich viele Frauen als emotionell empfindsamer, zugänglicher und berührbarer. Moderatorin und Sängerin Lina Berger nimmt’s mit Humor. Sie nennt die Wechseljahre ihren „inneren Sommer“ und träumt von einer implantierten Klimaanlage.</p>

  <div class="rule" style="top:932px"></div>
  <p class="contact" style="left:47px; top:962px"><strong>Anmeldung unter:</strong><br>www.lebensmitte-tag.ch /<br>info@wandel-raum.ch / 079 / 41 62 097</p>
  <p class="contact" style="left:47px; top:1052px"><span class="name">Marlene Ostwald</span><br>Dipl. Wechseljahresberaterin,<br>Sexualtherapeutin und Mentaltrainerin<br>www.Wandel-raum.ch&nbsp; Felsach</p>

  <h2 style="left:448px; top:52px">Wenn Sie erfahren möchten,</h2>
  <ul style="left:464px; top:104px; width:350px">
    <li>wie sich Ihr Körper in den Wechseljahren verändert,</li>
    <li>welche Beschwerden dadurch verursacht werden können</li>
    <li>was Sie aktiv zur Linderung und Vorbeugung beitragen können,</li>
    <li>wie Sie Ihre eigene Balance und Heilung finden</li>
  </ul>

  <div class="portrait" role="img" aria-label="Foto einer lächelnden älteren Frau mit grauem Haar, das Kinn auf die Hände gestützt"></div>

  <h2 style="left:448px; top:322px">Wollen Sie wissen:</h2>
  <ul class="pink" style="left:448px; top:372px; width:300px">
    <li>Was mit Ihnen passiert und wie Sie diese neue Lebensphase auf natürliche Weise bewältigen und annehmen können</li>
    <li>Worum es wirklich geht in diesen Jahren</li>
    <li>Wie Sie mutig und lustvoll durch die Wechseljahre kommen</li>
    <li>Mehr wissen über Östrogene, Progesterone und Testosterone</li>
  </ul>

  <div class="details" style="top:626px">Datum: 23.04.2017</div>
  <div class="details" style="top:674px">Seminar von 9.00 – 15.00 Uhr<br>Ort: Bildungshaus Sonnenrain,<br>3930 Talmatt<br>Kosten Seminar inkl. Getränke,<br>Obst, Z’Nüni und 4 Gang</div>

  <div class="badge">
    <p>Dieser Tag macht Mut zum Aufbruch und Neugier auf diese neue Lebensphase. Sie erleben, wie es sein wird, Altes loszulassen, den Blick nach vorn zu richten und wichtige Weichen für Ihren weiteren Lebensweg zu stellen.</p>
  </div>
</div>
</body>
</html>
```